8.5 x 11 Two Sided Flyer with our coffee descriptions/images

See www.BrindleKettle.com for elements and design look.

I have need to put all of our coffee bags onto a flyer with a brief description of each.

The header title should have the logo and the words Brindle Kettle Co.
Underneath a paragraph that states:
Located in the hills of Harlow County, Oregon, our small-batch craft coffees are freshly-roasted from responsibly sourced beans to ensure premium quality and taste. Retail: $19.95 for a full 16 oz. pound of freshly roasted ground or whole bean coffee. Wake up to better coffee with Brindle Kettle!

Then below, a small image of each of the coffees with their descriptions. SEE THE BOTTOM OF THIS PROJECT DESCRIPTION

At the very bottom, the url - www.BrindleKettle.com

The coffees should remain in the order provided.

FELICE SERA - Italian Roast
Hints of Dark Chocolate and Raspberry

From the hillsides of Tuscany to the waters of the Amalfi coast to the architecture of Rome, Italy is one of the most beautiful countries in the world.

Whether it’s high fashion and fast cars or fine wine an extra-virgin olive oil, the word “Italian” is synonymous with quality and the enjoyment of life’s finer things. As an old Italian proverb urges, “If you cannot live longer, live deeper.”

Following in the footsteps of his great-grandfather Enzo, Marco Dellatesta is a second generation Italian-American entrepreneur with a passion for living life to the fullest. A successful businessman, Enzo had a steel-like work ethic that fueled his vision. He saw opportunity, and through hard work and determination, would soon see it thrive. Volumes could be written about all that Italians like Enzo have contributed to the world.

When you walk the streets of Italy, you’ll also discover that Italians know no strangers. If you take the opportunity to visit one of the many cafes in any Italian city, you’ll be greeted with warm and sincere hospitality. “Felice Sera!” You’ll be offered gelato, a cannoli, likely a robust cup of caffé. Italians love their coffee almost as much as their wine. By the time you regretfully move on, you will be among friends.

To this end, we proclaim “Felice Sera,” and invite you to take a moment to live deeply and enjoy this robust Italian roast with us, your new friends, before you tackle life’s newest adventure.

Ciao.

ARCADIA - 4 X Caffeine - Sumatran & Indian

Arcadia: The afterlife where the chosen, the righteous, and the heroic indulge in everlasting pleasure. Compare to Grave Oath coffee.

This propriety blend is shown to possess more than four times the caffeine content of your standard cup. Experience the divinely bold coffee cup that results from exotic, dark-roasted Sumatran and Indian beans, where earthy notes and mild acidity balance to produce a rich, heavy body.

Why wish for death when you can experience Arcadia?

BANNER - Medium-Dark Roast Blend - Africa & Central America
Bold and hearty with notes of cocoa

Banner Blend celebrates the “melting pot” quality that gives our United States vitality.

The Banner Blend is intentionally mixed and roasted to be bold, the way we’d like all coffee to be. It begins with a refreshing balance of the best beans from Central America and Africa, and ends with a flavor only roasting in America can provide.

The specific flavors of this blend will vary from season to season, as all good coffees do, with coffee farming and cultivation ever changing throughout the year. But the essence of American craftsmanship will always ring true in this blended roast.

We wanted a coffee dedicated to American ideals. We wanted a drink worthy of our Founding Fathers; a drink we’d gladly brew in the great American tradition of consuming coffee—going all the way back to the Boston Tea Party.
After countless roasting sessions and tasting cup after cup of coffee, we settled on a combination of medium-dark roasted and dark roasted beans (we suspect James Madison made his the same way). The resulting blend is technically known as a melange, but we still call it a blend; one in keeping with the diverse and blended nature of our favorite constitutional republic.

DRIFTER - Decaf Medium-Dark Roast - Guatemala
Herbal and sweet with notes of caramel

Wind down with our fragrant and luscious decaf. Its complex aroma and smooth, sweet taste are a great way to start your decaffeinated day. Pairs well with chocolate or sugar cookies. Try it iced with your favorite syrup and whipped cream for a decadent, soothing indulgence.

Sleep easy knowing Drifter is always Alpine Brook Processed and never chemically decaffeinated.

TIMBERLINE - Medium Roast - Ethiopia
Bright and vibrant with notes of blueberry

The first TIMBERLINE Act of 1862 gave plots of land to farmers in the federally-owned properties of the West. The kinds of people who took advantage of this offer had a unique combination of traits.

On one hand, they were adventurous enough to leave the “settled” lands and move to the frontier. On the other hand, these were people looking for homes. They wanted to settle down, start families, and send down deep roots.

The Timberline Roast honors that curious combination of traits. It’s a member of the Brindle Kettle family, so you know it’s not going to be the coffee-as-usual you might expect from other roasters. It’s dauntless in that way.

But it’s also comfortable and cordial. The Timberline Roast just might put the word “hearth” in mind. Or “front porch.” That works too.

Vibrant and spirited, with citrus acidity and a smooth finish, the Timberline Roast is deliciously versatile. It wakes you up in the morning and facilitates your after-dinner conversation.

Timberline Roast brews up a golden brown, but it’s not overpowering. In fact, you might call it hospitable, because it always makes room for sugar and cream – or flavored syrup, if that’s your thing.

Even if you prefer a darker roast for yourself, the Timberline Roast makes a great addition to your home or business pantry to ensure you always have a satisfying, rich cup of coffee right in the comfort zone of most coffee drinkers.

WAYFARER - Medium-Dark Roast - Bolivia
Sweet and citric with notes of almond

America has always had more than its fair share of pioneers. From Daniel Boone to Jimi Hendrix to Steve Jobs, there’s something in our DNA that drives us to do things a little differently.

But pioneers are nothing if not practical. Because a useless innovation is in many ways worse than a mediocre commonplace.

That’s why we named our medium-dark roast the Wayfarer. It’s bold, for sure. But it’s not brash. It’s for the pioneer in all of us—with one eye on the frontier, and the other on taking care of business.

Velvety and rich, with notes of tree nuts and cocoa, the versatile Wayfarer Roast strikes out into the unexplored territory of the bold roast profiles.

The medium-dark Wayfarer Roast plays double duty. A “Goldilocks” blend that’s not too dark or too light, its flexible flavor profile goes well with foods both savory and sweet.

If you opt for fried bacon and scrambled eggs for breakfast over a bowl of cold cereal or a bagel, you’ll find the Wayfarer Roast’s notes of earthiness and toasted grain pleasantly accent your rich, savory breakfast.

On the other fork, if you’re looking for a good coffee to drink with your decadent double-decker chocolate cake, you’ll find Wayfarer Roast’s touch of smokiness cuts through and complements your sugary treat.

BONANZA - Dark Roast - Burundi
Chocolatey with notes of cherry

American prospectors made it all the way to the coast. They were never able to shake that pilgrim feeling that there was something even better a little further West… just a bit further on.

When some settlers hunkered down and built houses in the fly-over states, the prospectors kept going. They were looking for gold. But they were really hoping for a dream.

The Bonanza Roast honors that tradition. Going well beyond first crack, our expert roasters take these intrepid beans all the way to oil-coated glory. This is a bean that goes the distance. For people who won’t settle for anything less.

This dark-roasted bean packs a serious punch. Not all beans can stand up to the intense roasting temperatures required to turn a green bean into a lean, mean, caffeine machine.

That’s why our single origin Bonanza Roast utilizes only the most robust beans from the mountains of Central Africa to give you the maximum in bean and roast flavor in one compact package.

But let’s face it. You’re drinking this coffee because you like the complexity and richness that only a dark bean can offer. Sure, this coffee will pair with food. But who cares? This is a coffee you drink on its own. You drink it black.

You listen to music. You light your pipe, your cigar, your fire. This will keep you going. No matter what your prospects.

OUTPOST - Medium-Dark Roast - India, Ethiopia, Brazil
Hearty and nutty with a berry finish

Saddle up with a savory, complex and decadent roast. Perfect for all your favorite espresso drinks! Outpost can also be prepared without an espresso machine. Explore the expansive flavor profile with your preferred brewing method.

Outpost is blended with the finest beans from India, Ethiopia and Brazil. This espresso offers a hearty mouthfeel with a sweet berry finish.

DEREK MOANA’S RIPTIDE - Dark Roast - Brazil, Sumatra, Kenya

“This dark roast is what is I crave from a cup of coffee. Big, full-bodied, and bold. My exotic blend is made from responsibly sourced Brazilian, Sumatran and Kenyan beans. This coffee is the perfect way to embrace a beautiful day. Mahalo!” – Derek Moana

DEREK MOANA’S ROCKET - Medium 2X Caffeine - Sumatra, India
“Rocket is my nickname, because I go fast and head first into what I love. It takes a special coffee to tackle the biggest waves. Be warned this coffee has more than double the caffeine of your standard cup. Responsibly sourced Sumatran & Indian beans bring balance to the scales of flavor and power. This coffee is the perfect way to tackle an epic day. Shoots!” – Derek Moana

Target Market(s)

Grocery buyers

Industry/Entity Type

Grocery

Font styles to use
Serif
Sans Serif

Requirements
Must have
• Uniformity in the size and font styles - pretend it's a catalog
Nice to have
• Elements of brown / gold / black
Should not have
• Do not use bright colors - this is a luxury market and coffee related, does not want bright or neon colors

```html
<!DOCTYPE html>
<html lang="en">
<head>
<meta charset="utf-8">
<title>Brindle Kettle Co. — Coffee Flyer</title>
<link rel="stylesheet" href="https://fonts.googleapis.com/css2?family=PT+Sans:wght@400;700&family=Crimson+Text:wght@400;600;700&display=swap">
<style>
  :root {
    --backdrop: #e6e6e6;
    --paper: #ecdcc0;
    --paper-deep: #e3cfae;
    --ink: #1e140e;
    --brick: #8e3322;
    --cream: #fbf1e2;
    --gold: #b98133;
    --wood-dark: #3d2c1e;
    --wood-light: #7a624a;
    --bird-brown: #a86a32;
  }
  * { margin: 0; padding: 0; box-sizing: border-box; }
  html, body { width: 900px; height: 1200px; overflow: hidden; }
  body { background: var(--backdrop); position: relative; font-family: "Crimson Text", serif; color: var(--ink); }

  .flyer {
    position: absolute; left: 33px; top: 38px; width: 835px; height: 1082px;
    background: radial-gradient(ellipse at 50% 40%, var(--paper) 0%, var(--paper-deep) 100%);
    box-shadow: 3px 4px 6px rgba(0,0,0,0.28);
    overflow: hidden;
  }

  .brand {
    position: absolute; left: 48px; top: 58px;
    display: flex; align-items: center; gap: 14px;
  }
  .brand-dot { width: 74px; height: 74px; border-radius: 50%; border: 4px solid var(--ink); }
  .brand-name {
    font-family: "PT Sans", sans-serif; font-weight: 700; font-size: 36px;
    letter-spacing: 1px; color: var(--ink); line-height: 1;
  }

  .intro {
    position: absolute; left: 454px; top: 0; width: 358px; height: 225px;
    background: var(--brick); border-bottom-left-radius: 14px;
    padding: 40px 22px 0 28px;
    font-family: "Crimson Text", serif; font-size: 17px; line-height: 19.6px; color: var(--cream);
  }
  .intro strong { font-weight: 700; }

  .coffee {
    position: absolute; left: 55px; top: 255px; width: 730px;
  }
  .coffee-bag {
    position: absolute; left: 2px; top: 0; width: 66px; height: 219px;
    background: linear-gradient(180deg, #5a3f2c 0%, #3e2a1d 60%, #6a4e38 100%);
    box-shadow: 2px 3px 4px rgba(0,0,0,0.3);
  }
  .coffee-copy {
    position: absolute; left: 142px; top: 0; width: 588px;
    font-size: 15.2px; line-height: 16.5px;
  }
  .coffee-copy p { margin-bottom: 16.5px; text-align: justify; }
  .coffee-copy .coffee-title { font-weight: 700; text-align: left; }

  .site-url {
    position: absolute; right: 50px; top: 853px;
    font-weight: 700; font-size: 13.5px;
  }
  .gold-rule {
    position: absolute; left: 0; top: 875px; width: 835px; height: 9px; background: var(--gold);
  }
  .wood-band {
    position: absolute; left: 0; top: 884px; width: 835px; height: 198px;
    background: linear-gradient(90deg, var(--wood-dark) 0%, var(--wood-light) 45%, #5c4532 75%, var(--wood-dark) 100%);
  }
  .wood-brand {
    position: absolute; left: 320px; top: 940px;
    display: flex; align-items: center; gap: 16px;
  }
  .wood-brand .brand-dot { width: 80px; height: 80px; border-color: #e7d9c4; opacity: 0.85; }
  .wood-brand .brand-name { color: #e7d9c4; font-size: 44px; }

  .mascot-art {
    position: absolute; left: 0; top: 800px; width: 240px; height: 282px;
    background: radial-gradient(ellipse at 30% 45%, #c98a45 0%, var(--bird-brown) 55%, #6b4020 100%);
    border-top-right-radius: 120px;
  }
</style>
</head>
<body>
  <main class="flyer">
    <header class="brand">
      <span class="brand-dot"></span>
      <span class="brand-name">Brindle Kettle Co.</span>
    </header>

    <section class="intro">
      Located in the hills of <strong>Harlow County, Oregon</strong>, our small-batch craft coffees are <strong>freshly-roasted</strong> from responsibly sourced beans to ensure <strong>premium quality &amp; taste</strong>. <strong>Retail: $19.95</strong> for a full 16 oz. pound of <strong>freshly roasted ground</strong> or <strong>whole bean coffee</strong>. Wake up to better coffee with <strong>Brindle Kettle!</strong>
    </section>

    <article class="coffee">
      <div class="coffee-bag" role="img" aria-label="Photo of the Felice Sera Italian Roast coffee bag"></div>
      <div class="coffee-copy">
        <p class="coffee-title">FELICE SERA - Italian Roast</p>
        <p>Hints of Dark Chocolate and Raspberry</p>
        <p>From the hillsides of Tuscany to the waters of the Amalfi coast to the architecture of Rome, Italy is one of the most beautiful countries in the world.</p>
        <p>Whether it’s high fashion and fast cars or fine wine an extra-virgin olive oil, the word “Italian” is synonymous with quality and the enjoyment of life’s finer things. As an old Italian proverb urges, “If you cannot live longer, live deeper.”</p>
        <p>Following in the footsteps of his great-grandfather Enzo, Marco Dellatesta is a second generation Italian-American entrepreneur with a passion for living life to the fullest. A successful business­man, Enzo had a steel-like work ethic that fueled his vision. He saw opportunity, and through hard work and determination, would soon see it thrive. Volumes could be written about all that Italians like Enzo have contributed to the world.</p>
        <p>When you walk the streets of Italy, you’ll also discover that Italians know no strangers. If you take the opportunity to visit one of the many cafes in any Italian city, you’ll be greeted with warm and sincere hospitality. “Felice Sera!” You’ll be offered gelato, a cannoli, likely a robust cup of caffé. Italians love their coffee almost as much as their wine. By the time you regretfully move on, you will be among friends.</p>
        <p>To this end, we proclaim “Felice Sera,” and invite you to take a moment to live deeply and enjoy this robust Italian roast with us, your new friends, before you tackle life’s newest adventure.</p>
        <p>Ciao.</p>
      </div>
    </article>

    <div class="site-url">www.BrindleKettle.com</div>
    <div class="gold-rule"></div>
    <footer class="wood-band" role="img" aria-label="Photo of weathered wood planks with a coffee bag"></footer>
    <div class="wood-brand">
      <span class="brand-dot"></span>
      <span class="brand-name">Brindle Kettle Co.</span>
    </div>
    <div class="mascot-art" role="img" aria-label="Large brown bird-and-cup mascot illustration"></div>
  </main>
</body>
</html>
```